Redesign criminal justice consulting website

We run a small professional services firm that does research, evaluation, consulting, and training on criminal justice issues. We need to redesign our website (www.brvolquest.com). The existing site is something we made ourselves. It is unprofessional and does not do a good job of communicating what we do or who we are.

We would like the new site to provide a basic overview of what we do. Moreover, we would like it to communicate several themes that represent who we are:

* global

* innovative

* analytical

* practical

We view the principal design challenge as figuring out a subtle, interesting, and graphically appealing way to communicate these themes.

Target Market(s)

Our primary customers are governments, research firms, criminal justice agencies, and schools. The people who we want to find our site are seeking research, evaluation, training, or consulting services related to crime, criminal justice, or policing.

Industry/Entity Type

Consulting

Number of Pages Required

2 pages

Requirements
Must have
• 1. We would like the site to use our logo. It is attached (please use the maroon 4-color version with the company name but without the slogan). The site should also use the colors present in our logo. It may use other colors as well, as long as these colors coordinate with the logo colors.

• 2. For main pages or buttons, we need the following:
• *Home
• *About BVQ
• *Services
• *E-Training
• *Resources
• *Contact BVQ

• 3. We like simple, crisp, subtle designs over "busier," cluttered, or very complex designs.

• 4. We'd like to receive, at a minimum, the home page and a sample inner page.
Nice to have
• We need some help in thinking through what regions or sections should exist on the home page. We are thinking about having a window on there where we can make announcements about recent developments like new reports, new e-training videos, new photographs, etc... We are open to suggestions here.
Should not have
• 1. Gimmicky or overused clipart.
• 2. Cliched images associated with criminal justice, including magnifying glasses, scales of justice, etc... Our logo makes a subtle nod to criminal justice through the use of a fingerprint as the dot on the "J" in the company initials. That''s sufficient for our purposes. Concentrate instead on the themes listed above.
• 3. Major use of colors that don't match our logo, like blue.

```html
<!DOCTYPE html>
<html lang="en">
<head>
<meta charset="utf-8">
<title>BVQ – Bravo Quest Analysts</title>
<link href="https://fonts.googleapis.com/css2?family=PT+Serif:wght@400;700&family=Source+Sans+3:wght@400;600&display=swap" rel="stylesheet">
<style>
  :root{
    --maroon:#8a0b0b;
    --maroon-dark:#520005;
    --maroon-text:#9b1010;
    --beige-top:#f3e6d4;
    --beige-bottom:#e4d2b5;
    --ink:#1c1c1c;
    --muted:#a9a9a9;
    --rule:#3a3a3a;
    --white:#ffffff;
  }
  *{margin:0;padding:0;box-sizing:border-box}
  html,body{width:795px;height:1200px;overflow:hidden;background:var(--white)}
  body{font-family:"Source Sans 3",Arial,sans-serif;color:var(--ink)}
  .stage{position:relative;width:1351px;height:2040px;transform:scale(0.58846);transform-origin:0 0}
  .page{position:absolute;left:0;width:1351px}
  .page--home{top:0;height:1082px}
  .page--services{top:1119px;height:921px}
  .abs{position:absolute}

  .red-band{position:absolute;left:1px;right:0;top:93px;bottom:0;background:linear-gradient(var(--maroon),var(--maroon-dark))}
  .column{position:absolute;left:202px;width:950px;top:134px;bottom:0;background:var(--white)}

  .brand{position:absolute;left:234px;top:18px;display:flex;align-items:center;gap:12px;color:var(--maroon);font-family:"PT Serif",Georgia,serif;font-weight:700}
  .brand__dot{width:16px;height:16px;border-radius:50%;background:var(--maroon)}
  .brand__mark{font-size:50px;line-height:1}
  .brand__name{font-size:14px;line-height:1.15;letter-spacing:1.5px;width:120px}

  .search{position:absolute;left:862px;top:58px;display:flex;gap:8px}
  .search__field{width:206px;height:23px;border:1px solid var(--maroon);background:var(--white)}
  .search__btn{width:77px;height:24px;background:var(--maroon);color:var(--white);font:700 14px "PT Serif",Georgia,serif;display:flex;align-items:center;justify-content:center}

  .nav{position:absolute;top:95px;left:202px;width:950px;height:39px;font:700 15px "PT Serif",Georgia,serif;color:var(--white);letter-spacing:.3px}
  .nav span{position:absolute;top:11px}
  .nav i{position:absolute;top:4px;width:1px;height:32px;background:rgba(0,0,0,.25)}

  .hero{position:absolute;left:202px;top:134px;width:950px;height:364px;background:linear-gradient(var(--beige-top),var(--beige-bottom))}
  .hero__title{position:absolute;left:40px;top:36px;width:530px;text-align:center;font:400 50px/54px "PT Serif",Georgia,serif;color:var(--maroon)}
  .hero__rule{position:absolute;left:68px;top:167px;width:470px;height:1px;background:linear-gradient(90deg,transparent,#b79c77,transparent)}
  .hero__text{position:absolute;left:40px;top:192px;width:520px;text-align:center;font-size:17px;line-height:22px;color:#111}
  .btn{position:absolute;left:184px;top:283px;width:230px;height:44px;background:linear-gradient(#a31414,var(--maroon-dark));border:1px solid #5a0000;color:var(--white);font:700 18px "PT Serif",Georgia,serif;display:flex;align-items:center;justify-content:center}
  .hero__visual{position:absolute;left:624px;top:20px;width:256px;height:316px;border-radius:128px 128px 60px 60px;background:radial-gradient(circle at 50% 38%,#fbf6ee 0,#efe4d3 55%,rgba(228,210,181,0) 72%)}

  .section-title{position:absolute;font:400 25px "PT Serif",Georgia,serif;color:var(--maroon)}
  .feed-head{position:absolute;top:570px;height:33px;border-top:1px solid var(--rule);border-bottom:1px solid var(--rule);font:400 18px/31px "PT Serif",Georgia,serif;color:#111}
  .feed-head svg{position:absolute;right:4px;top:7px}
  .report{position:absolute;left:233px;width:360px;font-size:13px;line-height:17px}
  .report__thumb{position:absolute;left:1px;top:0;width:92px;height:69px;border:1px solid #e2d2b8;background:linear-gradient(135deg,#f4f7fa,#cfe2f1 60%,#e9f0f6)}
  .report__title{margin-left:106px;font-size:17px;line-height:20px;color:var(--maroon-text)}
  .report__lead{margin-left:106px;margin-top:3px}
  .more{display:block;font-weight:600;font-size:13px;color:var(--maroon-text)}
  .video{position:absolute;width:207px;height:114px;background:linear-gradient(135deg,#2e5f93,#9cc1e0 55%,#dbe9f5)}
  .caption{position:absolute;width:215px;font-size:13px;line-height:17px;color:var(--maroon-text)}
  .photo{position:absolute;width:111px;height:74px}
  .photo--lake{background:linear-gradient(#c9d3dc,#aab6c0 55%,#6e7a82)}
  .photo--dusk{background:linear-gradient(#c8a9b9,#e2b7a6 55%,#6c5a3a)}
  .photo--park{background:linear-gradient(#5f7d55,#8fa087 50%,#c9ccc9)}

  .footer{position:absolute;left:234px;width:888px;height:92px;border-top:1px solid #e6e6e6;background:linear-gradient(#ececec,#ffffff);text-align:center;font-family:"PT Serif",Georgia,serif;color:var(--muted)}
  .footer__links{margin-top:26px;font-size:12px;font-weight:700}
  .footer__links b{font-weight:400;margin:0 5px}
  .footer__copy{margin-top:8px;font-size:12px}

  .intro{position:absolute;left:202px;top:134px;width:950px;height:179px;background:linear-gradient(#f8efe3,#efe3d0)}
  .intro__text{position:absolute;left:34px;top:76px;width:880px;font-size:13px;line-height:17px}
  .lede{position:absolute;left:237px;top:356px;width:880px;font:400 19px/22px "PT Serif",Georgia,serif;color:#111}
  .practice{position:absolute;top:453px;font-size:13px;line-height:17px}
  .practice__title{font-size:17px;line-height:21px;color:var(--maroon-text);margin-bottom:12px}
  .practice .more{margin-top:18px}
  .divider{position:absolute;top:450px;width:1px;height:285px;background:#e1d4c2}
</style>
</head>
<body>
<div class="stage">

  <!-- Home page -->
  <section class="page page--home">
    <div class="brand"><span class="brand__dot"></span><span class="brand__mark">BVQ</span><span class="brand__name">BRAVO QUEST ANALYSTS</span></div>
    <div class="search"><div class="search__field"></div><div class="search__btn">Search</div></div>
    <div class="red-band"></div>
    <div class="column"></div>
    <nav class="nav">
      <span style="left:32px">HOME</span><i style="left:119px"></i>
      <span style="left:159px">ABOUT BVQ</span><i style="left:284px"></i>
      <span style="left:323px">SERVICES</span><i style="left:439px"></i>
      <span style="left:475px">E-TRAINING</span><i style="left:609px"></i>
      <span style="left:647px">RESOURCES</span><i style="left:783px"></i>
      <span style="left:815px">CONTACT BVQ</span>
    </nav>

    <div class="hero">
      <h1 class="hero__title">INNOVATIONS IN CRIME PREVENTION</h1>
      <div class="hero__rule"></div>
      <p class="hero__text">We specialize in working closely with our clients to design tailored, innovative solutions.<br>Call today and explore how we can be of service.</p>
      <div class="btn">CONTACT BVQ</div>
      <div class="hero__visual" role="img" aria-label="Globe assembled from outlined puzzle pieces with a soft reflection"></div>
    </div>

    <h2 class="section-title" style="left:234px;top:517px">OUR RECENT DEVELOPMENTS</h2>

    <div class="feed-head" style="left:233px;width:368px">REPORTS
      <svg width="20" height="20" viewBox="0 0 20 20"><circle cx="10" cy="10" r="10" fill="#8a0b0b"/><path d="M5 10h7M9 6l4 4-4 4" stroke="#fff" stroke-width="2.4" fill="none"/></svg></div>
    <div class="feed-head" style="left:626px;width:228px">E-TRAINING VIDEOS
      <svg width="20" height="20" viewBox="0 0 20 20"><circle cx="10" cy="10" r="10" fill="#8a0b0b"/><path d="M5 10h7M9 6l4 4-4 4" stroke="#fff" stroke-width="2.4" fill="none"/></svg></div>
    <div class="feed-head" style="left:882px;width:241px">PHOTOGRAPHS
      <svg width="20" height="20" viewBox="0 0 20 20"><circle cx="10" cy="10" r="10" fill="#8a0b0b"/><path d="M5 10h7M9 6l4 4-4 4" stroke="#fff" stroke-width="2.4" fill="none"/></svg></div>

    <article class="report" style="top:612px">
      <div class="report__thumb" role="img" aria-label="Rising arrows chart illustration"></div>
      <h3 class="report__title">Lorem ipsum dolor sit amet.</h3>
      <p class="report__lead">Lorem ipsum dolor sit amet, consectetur adipiscing elit. Praesent eget tortor tellus. Donec eu dui at mi suscipit lobortis.</p>
      <p>Etiam sed justo turpis, pellentesque venenatis nisl. In iaculis adipiscing mauris, id congue massa consectetur sed.</p>
      <a class="more" style="margin-top:13px">Read more &gt;&gt;</a>
    </article>
    <article class="report" style="top:777px">
      <div class="report__thumb" role="img" aria-label="Rising arrows chart illustration"></div>
      <h3 class="report__title">Lorem ipsum dolor sit amet.</h3>
      <p class="report__lead">Lorem ipsum dolor sit amet, consectetur adipiscing elit. Praesent eget tortor tellus. Donec eu dui at mi suscipit lobortis.</p>
      <p>Etiam sed justo turpis, pellentesque venenatis nisl. In iaculis adipiscing mauris, id congue massa consectetur sed.</p>
      <a class="more" style="margin-top:13px">Read more &gt;&gt;</a>
    </article>

    <div class="video" style="left:637px;top:614px" role="img" aria-label="Hand pointing a pen at a printed chart"></div>
    <p class="caption" style="left:636px;top:734px">Lorem ipsum dolor sit amet, conse ctetur adipiscing elit.</p>
    <div class="video" style="left:635px;top:779px" role="img" aria-label="Hand pointing a pen at a printed chart"></div>
    <p class="caption" style="left:635px;top:902px">Lorem ipsum dolor sit amet, conse ctetur adipiscing elit.</p>

    <div class="photo photo--lake" style="left:884px;top:614px" role="img" aria-label="Lakeside pier photo"></div>
    <div class="photo photo--dusk" style="left:1011px;top:614px" role="img" aria-label="Field at dusk photo"></div>
    <div class="photo photo--park" style="left:884px;top:704px" role="img" aria-label="Campus entrance photo"></div>
    <div class="photo photo--lake" style="left:1011px;top:704px" role="img" aria-label="Lakeside pier photo"></div>
    <div class="photo photo--dusk" style="left:884px;top:795px" role="img" aria-label="Field at dusk photo"></div>
    <div class="photo photo--park" style="left:1011px;top:795px" role="img" aria-label="Campus entrance photo"></div>

    <footer class="footer" style="top:990px">
      <p class="footer__links">Home<b>|</b>About BVQ<b>|</b>Copyright Information<b>|</b>Privacy Policy<b>|</b>Contact BVQ</p>
      <p class="footer__copy">Copyright 2010, Bravo Quest Analysts, Inc. All Rights Reserved.</p>
    </footer>
  </section>

  <!-- Services page -->
  <section class="page page--services">
    <div class="brand"><span class="brand__dot"></span><span class="brand__mark">BVQ</span><span class="brand__name">BRAVO QUEST ANALYSTS</span></div>
    <div class="search"><div class="search__field"></div><div class="search__btn">Search</div></div>
    <div class="red-band" style="top:94px"></div>
    <div class="column"></div>
    <nav class="nav">
      <span style="left:32px">HOME</span><i style="left:119px"></i>
      <span style="left:159px">ABOUT BVQ</span><i style="left:284px"></i>
      <span style="left:323px">SERVICES</span><i style="left:439px"></i>
      <span style="left:475px">E-TRAINING</span><i style="left:609px"></i>
      <span style="left:647px">RESOURCES</span><i style="left:783px"></i>
      <span style="left:815px">CONTACT BVQ</span>
    </nav>

    <div class="intro">
      <h1 class="section-title" style="left:32px;top:18px;font-size:30px">SERVICES</h1>
      <p class="intro__text">BVQ specializes in offering a suite of related services to its clients. A common trajectory is for BVQ to conduct an initial study or needs assessment, make a series of recommendations, work closely with agency staff to implement those recommendations, provide training and technical assistance throughout the implementation process, and then evaluate the success of the initiative. The results of the evaluation are then used to inform current practices and adjust strategic planning efforts. We believe this ongoing circular process of analysis, implementation, and evaluation is vital for transforming organizations and systems.</p>
    </div>

    <p class="lede">BVQ's four core practice areas reflect our underlying belief in the analytical process necessary for transforming organizations and systems.</p>

    <div class="practice" style="left:236px;width:185px">
      <h3 class="practice__title">Research, Evaluation, &amp; Assessment</h3>
      <p>BVQ has considerable expertise in research, evaluation, and assessment using a variety of qualitative and quantitative methods.</p>
      <a class="more">Learn more &gt;&gt;</a>
    </div>
    <div class="divider" style="left:437px"></div>
    <div class="practice" style="left:457px;width:200px">
      <h3 class="practice__title">Strategic Planning</h3>
      <p style="margin-top:30px">Today's criminal justice systems are complex and dynamic entities that rely on multiple agencies with different capacities and goals, personnel from various professional and personal backgrounds, and rapidly emerging changes in technology and tools.</p>
      <a class="more">Learn more &gt;&gt;</a>
    </div>
    <div class="divider" style="left:673px"></div>
    <div class="practice" style="left:692px;width:215px">
      <h3 class="practice__title">Training</h3>
      <p style="margin-top:32px">We have provided training on a variety of topics, including those listed below:</p>
      <p style="margin-top:17px;padding-left:8px">- Strategic crime control<br>- Criminal investigations<br>- Crime analysis<br>- Intelligence analysis<br>- Crime prevention<br>- Community policing<br>- Problem-oriented policing<br>- Addressing gang &amp; gun violence</p>
      <a class="more">Learn more &gt;&gt;</a>
    </div>
    <div class="divider" style="left:930px"></div>
    <div class="practice" style="left:947px;width:180px">
      <h3 class="practice__title">Technical Assistance</h3>
      <p style="margin-top:32px">Sometimes training alone is not enough. Agencies can benefit from onsite coaching or technical assistance on a variety of issues. Our team of experts can provide various forms of technical assistance ranging from brief or periodic onsite assessment and coaching to implanting experts full-time in your agency.</p>
      <a class="more">Learn more &gt;&gt;</a>
    </div>

    <footer class="footer" style="top:824px">
      <p class="footer__links">Home<b>|</b>About BVQ<b>|</b>Copyright Information<b>|</b>Privacy Policy<b>|</b>Contact BVQ</p>
      <p class="footer__copy">Copyright 2010, Bravo Quest Analysts, Inc. All Rights Reserved.</p>
    </footer>
  </section>

</div>
</body>
</html>
```